Building Maintenance Company Capability Statement

We would like a capability statement designed please.

Let us know where we can supply the written text.

Ideally, most of the information will be on our website.
www.tidewellgroup.com.au

Target Market(s)

Strata and building managers. schools and educational facilities, retirement and aged care.

Industry/Entity Type

Building

Font styles to use
Other font styles liked:
• nanito sans light

Requirements
Must have
• Images of people working (we can supply)
Easy to skim read
Colourful and attractive
Should not have
• lots of words

```html
<!DOCTYPE html>
<html lang="en">
<head>
<meta charset="utf-8">
<title>Tidewell Maintenance Solutions – Building and Painting Maintenance</title>
<link href="https://fonts.googleapis.com/css2?family=Montserrat:ital,wght@0,600;0,700;1,800;1,900&family=Nunito+Sans:wght@400;600&display=swap" rel="stylesheet">
<style>
  :root {
    --red: #d21f2d;
    --red-bright: #ec2229;
    --navy: #0b4479;
    --blue: #0a8ad0;
    --yellow: #ffe500;
    --white: #ffffff;
    --ink: #1d2b44;
    --icon: #124b86;
    --stage: #e9edf2;
  }
  * { box-sizing: border-box; margin: 0; padding: 0; }
  html, body { width: 1200px; height: 800px; overflow: hidden; }
  body {
    background: var(--stage);
    font-family: "Nunito Sans", sans-serif;
    position: relative;
  }
  .flyer {
    position: absolute;
    left: 330px; top: 18px;
    width: 540px; height: 764px;
    background: var(--white);
    overflow: hidden;
    box-shadow: 0 6px 24px rgba(0,0,0,.18);
  }
  .flyer-shapes { position: absolute; inset: 0; }
  .brand {
    position: absolute; left: 38px; top: 44px;
    display: flex; align-items: center; gap: 10px;
  }
  .brand-dot {
    width: 38px; height: 38px; border-radius: 50%;
    border: 4px solid var(--white);
  }
  .brand-name {
    font-family: "Montserrat", sans-serif;
    font-weight: 700; font-size: 17px; line-height: 1.15;
    color: var(--white); letter-spacing: .5px;
  }
  .headline {
    position: absolute; left: 38px; top: 118px;
    font-family: "Montserrat", sans-serif;
    font-style: italic; font-weight: 900;
    font-size: 31px; line-height: 33px; letter-spacing: -1.2px;
    color: var(--white); text-transform: uppercase;
  }
  .headline .accent { color: var(--yellow); display: block; }
  .tagline {
    position: absolute; left: 38px; top: 313px; width: 320px;
    font-family: "Montserrat", sans-serif;
    font-weight: 700; font-size: 19px; line-height: 25px;
    color: var(--white);
  }
  .services-title {
    position: absolute; left: 105px; top: 418px;
    width: 330px; height: 39px; border-radius: 20px;
    background: var(--red-bright);
    font-family: "Montserrat", sans-serif;
    font-style: italic; font-weight: 800; font-size: 21px;
    letter-spacing: -.8px;
    color: var(--white); text-align: center; line-height: 39px;
  }
  .services {
    position: absolute; left: 32px; top: 480px; width: 476px;
    display: grid; grid-template-columns: repeat(5, 1fr);
    row-gap: 22px;
  }
  .service { text-align: center; }
  .service svg {
    width: 40px; height: 40px; display: block; margin: 0 auto 8px;
    fill: none; stroke: var(--icon); stroke-width: 2; stroke-linecap: round; stroke-linejoin: round;
  }
  .service-label {
    font-size: 10.5px; line-height: 13px; color: var(--ink);
  }
  .contact {
    position: absolute; left: 0; right: 0; top: 718px;
    display: flex; justify-content: center; gap: 26px;
    color: var(--white); font-size: 12.5px;
  }
  .contact-item { display: flex; align-items: center; gap: 7px; }
  .contact-icon {
    width: 20px; height: 20px; border-radius: 50%; background: var(--white);
    display: flex; align-items: center; justify-content: center;
  }
  .contact-icon svg { width: 12px; height: 12px; fill: none; stroke: var(--red-bright); stroke-width: 2; }
</style>
</head>
<body>
<main class="flyer">
  <svg class="flyer-shapes" viewBox="0 0 540 764" width="540" height="764">
    <defs>
      <linearGradient id="site-photo" x1="0" y1="0" x2="1" y2="1">
        <stop offset="0" stop-color="#a88a62"/>
        <stop offset=".5" stop-color="#8c9aa3"/>
        <stop offset="1" stop-color="#c9b98f"/>
      </linearGradient>
      <linearGradient id="fence-photo" x1="0" y1="0" x2="1" y2="1">
        <stop offset="0" stop-color="#cbbd6a"/>
        <stop offset=".5" stop-color="#7b6f5c"/>
        <stop offset="1" stop-color="#9a9088"/>
      </linearGradient>
    </defs>
    <path class="navy-panel" d="M0,230 H540 V417 Q540,437 520,437 H20 Q0,437 0,417 Z" fill="var(--navy)"/>
    <path class="accent-band" d="M0,362 Q300,382 540,250 L540,264 Q300,398 0,376 Z" fill="var(--blue)"/>
    <path class="red-panel" d="M0,0 H540 V250 Q300,382 0,362 Z" fill="var(--red)"/>
    <g role="img" aria-label="Photo of a tradesman on a ladder renovating a house exterior">
      <circle cx="478" cy="38" r="182" fill="url(#site-photo)" stroke="var(--white)" stroke-width="8"/>
    </g>
    <g role="img" aria-label="Photo of a worker repairing a timber fence with a nail gun">
      <circle cx="456" cy="305" r="90" fill="url(#fence-photo)" stroke="var(--white)" stroke-width="7"/>
    </g>
    <circle class="ring" cx="331" cy="258" r="28" fill="none" stroke="var(--white)" stroke-width="2.5"/>
    <path class="footer-accent" d="M0,712 Q250,650 540,668 V764 H0 Z" fill="var(--red-bright)"/>
    <path class="footer-panel" d="M0,724 Q250,668 540,680 V764 H0 Z" fill="var(--navy)"/>
  </svg>

  <div class="brand">
    <span class="brand-dot"></span>
    <span class="brand-name">TIDEWELL<br>MAINTENANCE SOLUTIONS</span>
  </div>

  <h1 class="headline">Building<br>and Painting<span class="accent">Maintenance</span></h1>

  <p class="tagline">We Provide Cost Effective Solutions To Your Building And Maintenance Requirements.</p>

  <h2 class="services-title">OUR SERVICES</h2>

  <section class="services">
    <div class="service">
      <svg viewBox="0 0 40 40"><rect x="8" y="4" width="24" height="9" rx="2"/><path d="M32 8h3v10H20v5"/><rect x="18" y="23" width="4" height="13" rx="2"/></svg>
      <p class="service-label">Internal and external Painting</p>
    </div>
    <div class="service">
      <svg viewBox="0 0 40 40"><path d="M6 36h28M6 36l6-18h16l6 18M12 18l-2 18M17 18l-1 18M22 18l1 18M27 18l3 18"/><path d="M10 10v-6M8 6h4M28 12a4 4 0 0 1 8 0"/></svg>
      <p class="service-label">Landscaping and grounds maintenance</p>
    </div>
    <div class="service">
      <svg viewBox="0 0 40 40"><path d="M16 4h12v6H16zM20 10v4M16 14h10l4 8v14H12V22z"/><circle cx="21" cy="28" r="4"/><path d="M6 5h6M5 9h7M7 13h5"/></svg>
      <p class="service-label">Preventative and ongoing maintenance</p>
    </div>
    <div class="service">
      <svg viewBox="0 0 40 40"><path d="M4 26l6-16h20l6 16zM10 10l-3 16M16 10l-2 16M24 10l2 16M30 10l3 16M7 18h26"/><path d="M4 26q4 4 8 0q4 4 8 0q4 4 8 0q4 4 8 0"/></svg>
      <p class="service-label">Roofing repairs, repaints and replacements</p>
    </div>
    <div class="service">
      <svg viewBox="0 0 40 40"><path d="M4 8h22a6 6 0 0 1 0 12H14a6 6 0 0 0 0 12h22"/><path d="M4 5v6M36 29v6"/></svg>
      <p class="service-label">Plumbing Installation and Repair</p>
    </div>
    <div class="service">
      <svg viewBox="0 0 40 40"><path d="M23 4L11 22h9l-4 14 14-20h-9z"/></svg>
      <p class="service-label">Electrical</p>
    </div>
    <div class="service">
      <svg viewBox="0 0 40 40"><path d="M12 8a14 14 0 0 1 16 0M32 12a14 14 0 0 1 0 16M28 32a14 14 0 0 1-16 0M8 28a14 14 0 0 1 0-16"/><path d="M25 5l3 3-3 3M35 25l-3 3-3-3M15 35l-3-3 3-3M5 15l3-3 3 3"/></svg>
      <p class="service-label">Refurbishments</p>
    </div>
    <div class="service">
      <svg viewBox="0 0 40 40"><rect x="5" y="5" width="30" height="30"/><path d="M5 22h14V5M19 13h16M26 13v22M12 22v13"/></svg>
      <p class="service-label">Flooring</p>
    </div>
    <div class="service">
      <svg viewBox="0 0 40 40"><rect x="6" y="5" width="28" height="30" rx="2"/><rect x="10" y="9" width="20" height="22"/><path d="M14 13h.1M19 13h.1M24 13h.1M14 18h.1M19 18h.1M14 23h.1M22 28l6-6"/></svg>
      <p class="service-label">Plastering</p>
    </div>
    <div class="service">
      <svg viewBox="0 0 40 40"><path d="M4 30h32M4 35h32M6 30v5M34 30v5M14 26l16-16 4 4-16 16h-4z"/><path d="M10 8a3 3 0 1 1 0 6"/></svg>
      <p class="service-label">Carpentry</p>
    </div>
  </section>

  <footer class="contact">
    <div class="contact-item">
      <span class="contact-icon"><svg viewBox="0 0 12 12"><path d="M6 11S2 7 2 4.5a4 4 0 0 1 8 0C10 7 6 11 6 11z"/><circle cx="6" cy="4.5" r="1.3"/></svg></span>
      <span>4/22 Harlow Street, Elmridge QLD 4102</span>
    </div>
    <div class="contact-item">
      <span class="contact-icon"><svg viewBox="0 0 12 12"><path d="M3 1.5l2 2-1 1.5a6 6 0 0 0 3 3l1.5-1 2 2-1.5 1.5C5 10.5 1.5 7 1.5 3z"/></svg></span>
      <span>0400 318 702</span>
    </div>
  </footer>
</main>
</body>
</html>
```